SaaS Early tech startup business card design

Unique design for experience ecommerce platform company. the business cards will be used by executive members. conformance with color code is required.

```html
<!DOCTYPE html>
<html lang="en">
<head>
<meta charset="utf-8">
<title>Vamo Business Card</title>
<link href="https://fonts.googleapis.com/css2?family=Arimo:wght@400;700&display=swap" rel="stylesheet">
<style>
  :root {
    --bg: #c4c4c4;
    --white: #ffffff;
    --blue: #17649a;
    --teal: #0bbc9c;
    --teal-line: #2bb9a0;
    --ink: #3a3a3a;
  }
  * { margin: 0; padding: 0; box-sizing: border-box; }
  html, body { width: 1200px; height: 788px; overflow: hidden; }
  body {
    background: var(--bg);
    font-family: "Arimo", Arial, sans-serif;
    position: relative;
  }
  .card {
    position: absolute;
    width: 540px;
    height: 310px;
    border-radius: 18px;
    overflow: hidden;
    box-shadow: 0 10px 24px rgba(0,0,0,0.22);
  }
  .card-front { left: 40px; top: 239px; background: var(--white); }
  .card-back {
    left: 620px; top: 239px;
    background: linear-gradient(30deg, var(--blue) 0%, #0b8499 50%, var(--teal) 100%);
  }
  .edge-band {
    position: absolute; left: 0; right: 0; bottom: 0; height: 8px;
    background: var(--blue);
    border-top: 3px solid var(--teal);
  }
  .front-wordmark {
    position: absolute; left: 46px; top: 110px;
    font-weight: 700; font-size: 72px; letter-spacing: -2px;
    color: var(--blue); line-height: 1;
  }
  .divider {
    position: absolute; left: 258px; top: 62px; width: 1px; height: 170px;
    background: var(--teal-line);
  }
  .details { position: absolute; left: 282px; top: 56px; width: 230px; }
  .person-name { font-weight: 700; font-size: 19px; color: var(--blue); letter-spacing: 0.3px; }
  .person-name .surname { color: var(--teal); }
  .person-title { font-size: 12px; color: var(--ink); margin-top: 2px; }
  .rule { height: 1px; background: var(--teal-line); margin: 8px 0; }
  .address { font-size: 12px; color: var(--ink); line-height: 1.35; }
  .contact-list { list-style: none; font-size: 12px; color: var(--ink); line-height: 1.5; }
  .contact-list li { display: flex; align-items: center; gap: 6px; }
  .contact-list svg { width: 10px; height: 10px; flex: none; }
  .back-wordmark {
    position: absolute; left: 0; right: 0; top: 98px; text-align: center;
    font-weight: 700; font-size: 110px; letter-spacing: -3px;
    color: var(--white); line-height: 1;
  }
</style>
</head>
<body>
  <section class="card card-front" aria-label="Business card front">
    <div class="front-wordmark">vamo</div>
    <div class="divider"></div>
    <div class="details">
      <p class="person-name">DANA <span class="surname">ELLERY</span></p>
      <p class="person-title">Owner/CEO</p>
      <div class="rule"></div>
      <p class="address">212 - 4480 Harbour Ave<br>Langley, BC V2Y1K4</p>
      <div class="rule"></div>
      <ul class="contact-list">
        <li><svg viewBox="0 0 10 10"><path d="M2 1 L4 3 L3 4 Q4 6 6 7 L7 6 L9 8 L8 9 Q3 9 1 2 Z" fill="#17649a"/></svg>(604) 555 - 01827</li>
        <li><svg viewBox="0 0 10 10"><rect x="0.5" y="2" width="9" height="6" fill="#17649a"/><path d="M0.5 2 L5 5.5 L9.5 2" stroke="#fff" fill="none" stroke-width="0.8"/></svg>dana@orvelagroup.com</li>
        <li><svg viewBox="0 0 10 10"><circle cx="5" cy="5" r="4.5" fill="#17649a"/><path d="M0.5 5 H9.5 M5 0.5 Q2 5 5 9.5 M5 0.5 Q8 5 5 9.5" stroke="#fff" fill="none" stroke-width="0.7"/></svg>www.orvelagroup.com</li>
      </ul>
    </div>
    <div class="edge-band"></div>
  </section>

  <section class="card card-back" aria-label="Business card back">
    <div class="back-wordmark">vamo</div>
  </section>
</body>
</html>
```